Business Card

THIS IS THE CARD INFORMATION
DEVELOPMENT I FINANCING I PROPERTY MANAGEMENT
DANIEL FERRÁN
3186 NE 74th Terrace
Cedar Bay, FL 33419
Telephone I 855.274.6180
Facsimile I 855.274.6127
Industry/Entity Type
Business

```html
<!DOCTYPE html>
<html lang="en">
<head>
<meta charset="utf-8">
<title>Salcedo Vargas &amp; Company – Business Card</title>
<link rel="stylesheet" href="https://fonts.googleapis.com/css2?family=Open+Sans:wght@300;400;700&display=swap">
<style>
  :root {
    --page-bg: #e9e6e1;
    --card-white: #ffffff;
    --ink-dark: #2b2b2b;
    --ink-gray: #5a5a5a;
    --brand-purple: #9b1f86;
    --brand-purple-light: #b0529f;
    --band-dark: #2a0b24;
    --panel-center: #5f5f61;
    --panel-edge: #3f3f41;
    --text-light: #ffffff;
  }
  * { margin: 0; padding: 0; box-sizing: border-box; }
  html, body {
    width: 1200px; height: 770px; overflow: hidden;
    background: var(--page-bg);
    font-family: "Open Sans", Arial, sans-serif;
  }
  .card {
    position: absolute; left: 50px; top: 70px;
    width: 1100px; height: 630px;
    background: var(--card-white);
    box-shadow: 0 6px 18px rgba(0,0,0,.18);
    overflow: hidden;
  }
  .card-header { position: absolute; left: 0; top: 0; width: 100%; height: 243px; }
  .brand {
    position: absolute; left: 157px; top: 24px;
    display: flex; align-items: center; gap: 24px;
  }
  .brand-dot {
    width: 144px; height: 144px; border-radius: 50%;
    background: var(--brand-purple);
  }
  .brand-name {
    font-weight: 700; font-size: 60px; line-height: 1.05;
    color: var(--ink-dark); letter-spacing: -0.5px;
  }
  .services {
    position: absolute; left: 0; top: 180px; width: 100%;
    text-align: center; font-weight: 300; font-size: 38px;
    color: var(--ink-gray); letter-spacing: 0.2px; white-space: nowrap;
  }
  .services .divider { color: var(--brand-purple); font-weight: 400; padding: 0 1px; }
  .accent-band {
    position: absolute; left: 0; top: 243px; width: 100%; height: 22px;
    background: linear-gradient(90deg, var(--brand-purple), var(--brand-purple-light));
  }
  .accent-shadow {
    position: absolute; left: 0; top: 265px; width: 100%; height: 21px;
    background: var(--band-dark);
  }
  .contact-panel {
    position: absolute; left: 0; top: 286px; width: 100%; height: 344px;
    background: radial-gradient(ellipse at 50% 45%, var(--panel-center), var(--panel-edge) 75%);
    color: var(--text-light);
  }
  .holder-name {
    position: absolute; left: 0; top: 22px; width: 100%;
    text-align: center; font-weight: 300; font-size: 66px; letter-spacing: 1px;
  }
  .address {
    position: absolute; left: 0; top: 110px; width: 100%;
    text-align: center; font-weight: 300; font-size: 37px; line-height: 41px;
  }
  .contact-line {
    position: absolute; top: 204px; width: 300px;
    text-align: center;
  }
  .contact-line.phone { left: 67px; }
  .contact-line.fax { left: 729px; }
  .contact-icon { width: 76px; height: 76px; display: block; margin: 0 auto; }
  .contact-number {
    display: block; margin-top: 0;
    font-weight: 300; font-size: 38px; letter-spacing: 0.5px;
  }
</style>
</head>
<body>
  <main class="card">
    <header class="card-header">
      <div class="brand">
        <div class="brand-dot"></div>
        <div class="brand-name">SALCEDO VARGAS<br>&amp; COMPANY</div>
      </div>
      <p class="services">DEVELOPMENT <span class="divider">|</span> FINANCING <span class="divider">|</span> PROPERTY MANAGEMENT</p>
    </header>
    <div class="accent-band"></div>
    <div class="accent-shadow"></div>
    <section class="contact-panel">
      <h1 class="holder-name">DANIEL FERRÁN</h1>
      <p class="address">3186 NE 74TH TERRACE<br>CEDAR BAY, FL 33419</p>
      <div class="contact-line phone">
        <svg class="contact-icon" viewBox="0 0 78 78" role="img" aria-label="Telephone">
          <circle cx="39" cy="39" r="39" fill="#fff"/>
          <path d="M17 30 Q39 16 61 30 L58 37 L49 34 L48 29 Q39 26 30 29 L29 34 L20 37 Z" fill="#333"/>
          <path d="M27 38 L51 38 L58 58 L20 58 Z" fill="#333"/>
          <g fill="#fff">
            <rect x="30" y="43" width="4" height="3"/><rect x="37" y="43" width="4" height="3"/><rect x="44" y="43" width="4" height="3"/>
            <rect x="29" y="48" width="4" height="3"/><rect x="37" y="48" width="4" height="3"/><rect x="45" y="48" width="4" height="3"/>
            <rect x="28" y="53" width="4" height="3"/><rect x="37" y="53" width="4" height="3"/><rect x="46" y="53" width="4" height="3"/>
          </g>
        </svg>
        <span class="contact-number">855.274.6180</span>
      </div>
      <div class="contact-line fax">
        <svg class="contact-icon" viewBox="0 0 78 78" role="img" aria-label="Facsimile">
          <circle cx="39" cy="39" r="39" fill="#fff"/>
          <rect x="26" y="14" width="26" height="20" fill="#fff" stroke="#333" stroke-width="3"/>
          <g stroke="#333" stroke-width="2"><line x1="30" y1="21" x2="48" y2="21"/><line x1="30" y1="26" x2="48" y2="26"/></g>
          <rect x="16" y="32" width="46" height="22" rx="3" fill="#333"/>
          <rect x="24" y="50" width="30" height="12" fill="#333"/>
          <rect x="28" y="52" width="22" height="3" fill="#fff"/>
        </svg>
        <span class="contact-number">855.274.6127</span>
      </div>
    </section>
  </main>
</body>
</html>
```